Email Notification & Marketing Templates

I want to start with something like a newsletter or informational email, but i need Top Tips to Detect Phishing Scams. Something that i can send to users so they can follow it when receiving or exchanging emails. I will also need promotional items for my company that i can send to customers as well. It can be based on on our website QRVLINK.COM

Will also need:
newsletters
announcements
marketing emails
alerts
security notifications

Examples:Items such as Security Awareness Poster Series
Phishing Awareness
Password Security
Email Attachments
QR Code scams
Public WiFi safety

```html
<!DOCTYPE html>
<html lang="en">
<head>
<meta charset="UTF-8">
<title>Phishing Awareness Poster Series – QRVLINK</title>
<link href="https://fonts.googleapis.com/css2?family=Montserrat:wght@400;500;600;700;800&family=Audiowide&display=swap" rel="stylesheet">
<style>
  :root {
    --canvas-grey: #c4c4c4;
    --black: #000000;
    --white: #ffffff;
    --lime: #8fdc2c;
    --lime-pale: #c8ef8a;
    --green-deep: #138a1f;
    --green-mid: #3cae24;
    --alert-red: #e0301e;
    --text-dark: #1b1b1b;
    --text-soft: #d8d8d8;
    --muted: #b9b9b9;
  }
  * { box-sizing: border-box; margin: 0; padding: 0; }
  html, body { width: 890px; height: 1200px; overflow: hidden; }
  body {
    background: var(--canvas-grey);
    font-family: "Montserrat", Arial, sans-serif;
    position: relative;
  }

  /* ---------- Social tiles ---------- */
  .tile {
    position: absolute;
    left: 10px;
    width: 386px;
    height: 386px;
    background: var(--black);
    color: var(--white);
  }
  .tile--https-top { top: 11px; }
  .tile--sender { top: 408px; }
  .tile--https-bottom { top: 804px; }

  .tile__title {
    position: absolute;
    top: 50px;
    left: 0; right: 0;
    text-align: center;
    font-weight: 700;
    font-size: 30px;
    line-height: 35px;
    letter-spacing: -0.5px;
  }
  .tile__title .accent { color: var(--lime-pale); }

  .tile__art {
    position: absolute;
    left: 52px;
    top: 123px;
    width: 272px;
    height: 168px;
    border-radius: 40px 90px 60px 30px;
    background: radial-gradient(ellipse at 60% 50%, #8fdc2c 0%, #4caf2a 45%, #1d3a16 80%, #000 100%);
  }
  .tile--sender .tile__art {
    background: radial-gradient(ellipse at 60% 50%, #e8edf2 0%, #b6c7a6 40%, #4caf2a 70%, #000 100%);
  }

  .tile__caption {
    position: absolute;
    left: 30px; right: 30px;
    top: 309px;
    text-align: center;
    font-size: 8.6px;
    line-height: 11.5px;
    letter-spacing: -0.15px;
  }
  .tile--sender .tile__caption { top: 312px; }

  .tile__brand {
    position: absolute;
    right: 22px;
    bottom: 16px;
    display: flex;
    align-items: center;
    gap: 4px;
    font-weight: 800;
    font-size: 12px;
    color: var(--lime);
  }
  .brand-dot {
    width: 8px; height: 8px;
    background: var(--lime);
    border-radius: 50%;
  }

  /* ---------- Poster ---------- */
  .poster {
    position: absolute;
    left: 408px;
    top: 11px;
    width: 471px;
    height: 1178px;
    background: var(--white);
    overflow: hidden;
  }

  .poster__header {
    position: absolute;
    top: 0; left: 0;
    width: 100%;
    height: 83px;
    background: linear-gradient(100deg, #0b2a07 0%, #0a0a0a 45%, #000 100%);
  }
  .poster__brand {
    position: absolute;
    left: 34px;
    top: 24px;
    display: flex;
    align-items: center;
    gap: 7px;
    font-weight: 800;
    font-size: 24px;
    color: var(--green-mid);
    letter-spacing: 0.5px;
  }
  .poster__brand .brand-dot { width: 14px; height: 14px; background: var(--green-mid); }
  .poster__tagline {
    position: absolute;
    right: 28px;
    top: 29px;
    text-align: right;
    color: var(--muted);
    font-weight: 600;
    font-size: 12px;
    line-height: 14px;
  }

  .hero {
    position: absolute;
    top: 83px; left: 0;
    width: 100%;
    height: 214px;
    background: linear-gradient(100deg, #0f7f17 0%, #2b9a1f 45%, #86d23a 100%);
  }
  .hero__headline {
    position: absolute;
    left: 34px;
    top: 26px;
    color: var(--white);
    font-family: "Audiowide", "Montserrat", sans-serif;
    text-transform: uppercase;
    line-height: 1;
  }
  .hero__big { display: block; font-size: 52px; letter-spacing: -1px; margin-bottom: 4px; }
  .hero__mid { display: block; font-size: 27px; margin-top: 6px; letter-spacing: 0.5px; }
  .hero__small { display: block; font-size: 19px; margin-top: 8px; letter-spacing: 0px; }
  .hero__art {
    position: absolute;
    left: 268px;
    top: 46px;
    width: 192px;
    height: 168px;
    border-radius: 80px 80px 20px 20px;
    background: radial-gradient(ellipse at 50% 45%, #f4f8f4 0%, #cfe9c6 50%, rgba(143,220,44,0.4) 85%, rgba(143,220,44,0) 100%);
  }

  /* Red flag list */
  .flags {
    position: absolute;
    top: 318px;
    left: 0;
    width: 100%;
    list-style: none;
  }
  .flag {
    position: absolute;
    left: 0;
    width: 100%;
  }
  .flag__icon {
    position: absolute;
    left: 43px;
    top: 0;
    width: 52px;
    height: 52px;
  }
  .flag__body {
    position: absolute;
    left: 115px;
    right: 30px;
    top: 0;
  }
  .flag__title {
    font-weight: 700;
    font-size: 15.5px;
    color: var(--text-dark);
    margin-bottom: 4px;
    letter-spacing: -0.2px;
  }
  .flag__text {
    font-size: 9.4px;
    line-height: 12.6px;
    color: var(--text-dark);
  }
  .flag__text strong { font-weight: 700; }

  .flag--urgency { top: 16px; }
  .flag--sender  { top: 97px; }
  .flag--hover   { top: 186px; }
  .flag--attach  { top: 266px; }
  .flag--offers  { top: 338px; }

  /* Safety section */
  .safety {
    position: absolute;
    top: 734px; left: 0;
    width: 100%;
    height: 411px;
    background: var(--black);
  }
  .safety__glow {
    position: absolute;
    top: 0; left: 0;
    width: 100%;
    height: 145px;
    background: linear-gradient(100deg, #000 0%, #0c2a06 40%, #3f9b22 85%, #000 100%);
  }
  .safety__title {
    position: absolute;
    left: 43px;
    top: 38px;
    font-family: "Audiowide", "Montserrat", sans-serif;
    font-size: 35px;
    line-height: 43px;
    color: var(--lime);
    text-transform: uppercase;
  }
  .safety__art {
    position: absolute;
    left: 232px;
    top: 20px;
    width: 216px;
    height: 125px;
    border-radius: 60px 60px 0 0;
    background: radial-gradient(ellipse at 50% 55%, #eef2ee 0%, #c6cbc6 45%, rgba(120,170,70,0.5) 80%, rgba(0,0,0,0) 100%);
  }
  .tip {
    position: absolute;
    width: 175px;
  }
  .tip__title {
    font-weight: 700;
    font-size: 15px;
    line-height: 18px;
    color: var(--lime);
    margin-bottom: 9px;
    letter-spacing: -0.2px;
  }
  .tip__text {
    font-size: 9.2px;
    line-height: 11px;
    color: var(--text-soft);
    letter-spacing: -0.2px;
  }
  .tip--verify { left: 44px; top: 163px; }
  .tip--mfa    { left: 263px; top: 163px; width: 180px; }
  .tip--https  { left: 44px; top: 297px; }
  .tip--browser{ left: 263px; top: 297px; width: 180px; }

  .poster__footer {
    position: absolute;
    bottom: 0; left: 0;
    width: 100%;
    height: 33px;
    background: linear-gradient(90deg, #8fdc2c 0%, #3cae24 60%, #2e7d1d 100%);
    color: var(--white);
    font-weight: 700;
    font-size: 16px;
    letter-spacing: 2px;
    text-align: center;
    line-height: 33px;
  }
</style>
</head>
<body>

  <!-- Tile: Check for https -->
  <section class="tile tile--https-top">
    <h2 class="tile__title">Always <span class="accent">Check</span><br>for <span class="accent">https://</span></h2>
    <div class="tile__art" role="img" aria-label="Illustration of a masked hacker at a chained laptop, puzzled by an https:// label, beside green and grey diamond shapes"></div>
    <p class="tile__caption">Legitimate websites use secure, encrypted connections,<br>though this alone does not guarantee a site is safe.</p>
    <div class="tile__brand"><span class="brand-dot"></span>QRVLINK</div>
  </section>

  <!-- Tile: Verify sender -->
  <section class="tile tile--sender">
    <h2 class="tile__title"><span class="accent">Always Verify</span><br>Sender <span class="accent">Address</span></h2>
    <div class="tile__art" role="img" aria-label="Illustration of a woman checking her phone beside a large smartphone showing an email envelope, with a paper plane and a plant"></div>
    <p class="tile__caption">If you receive an urgent alert from a company, do not use the contact information in the email. Instead, find the company's official phone number or website separately.</p>
    <div class="tile__brand"><span class="brand-dot"></span>QRVLINK</div>
  </section>

  <!-- Tile: Check for https (repeat) -->
  <section class="tile tile--https-bottom">
    <h2 class="tile__title">Always <span class="accent">Check</span><br>for <span class="accent">https://</span></h2>
    <div class="tile__art" role="img" aria-label="Illustration of a masked hacker at a chained laptop, puzzled by an https:// label, beside green and grey diamond shapes"></div>
    <p class="tile__caption">Legitimate websites use secure, encrypted connections,<br>though this alone does not guarantee a site is safe.</p>
    <div class="tile__brand"><span class="brand-dot"></span>QRVLINK</div>
  </section>

  <!-- Poster -->
  <article class="poster">
    <header class="poster__header">
      <div class="poster__brand"><span class="brand-dot"></span>QRVLINK</div>
      <div class="poster__tagline">Managed<br>IT Services</div>
    </header>

    <section class="hero">
      <h1 class="hero__headline">
        <span class="hero__big">5 Red</span>
        <span class="hero__big">Flags</span>
        <span class="hero__mid">To Identify</span>
        <span class="hero__small">Phishing Scams</span>
      </h1>
      <div class="hero__art" role="img" aria-label="Illustration of a person with a laptop next to a large phone showing an email envelope, login form, chat bubbles and a megaphone"></div>
    </section>

    <ul class="flags">
      <li class="flag flag--urgency">
        <svg class="flag__icon" viewBox="0 0 52 52" aria-hidden="true">
          <g stroke="#111" stroke-width="2.2" stroke-linecap="round">
            <line x1="26" y1="2" x2="26" y2="8"/><line x1="10" y1="8" x2="14" y2="12"/><line x1="42" y1="8" x2="38" y2="12"/>
            <line x1="3" y1="24" x2="9" y2="24"/><line x1="43" y1="24" x2="49" y2="24"/>
          </g>
          <path d="M12 40 V28 a14 14 0 0 1 28 0 V40 Z" fill="var(--alert-red)" stroke="#111" stroke-width="2"/>
          <circle cx="26" cy="29" r="4" fill="none" stroke="#111" stroke-width="2"/>
          <line x1="26" y1="33" x2="26" y2="40" stroke="#111" stroke-width="2"/>
          <rect x="7" y="40" width="38" height="8" rx="1" fill="#111"/>
        </svg>
        <div class="flag__body">
          <h3 class="flag__title">Sense of Urgency or Threats</h3>
          <p class="flag__text">Scammers often demand immediate action, such as <strong>"your account will be suspended"</strong> or <strong>"urgent payment required,"</strong> to pressure you into skipping safety checks.</p>
        </div>
      </li>

      <li class="flag flag--sender">
        <svg class="flag__icon" viewBox="0 0 52 52" aria-hidden="true">
          <rect x="13" y="3" width="26" height="26" fill="#fff" stroke="#111" stroke-width="2"/>
          <path d="M4 20 L26 6 L48 20 V48 H4 Z" fill="var(--alert-red)" stroke="#111" stroke-width="2" stroke-linejoin="round"/>
          <rect x="13" y="8" width="26" height="20" fill="#fff" stroke="#111" stroke-width="2"/>
          <circle cx="26" cy="17" r="6" fill="none" stroke="var(--alert-red)" stroke-width="2.4"/>
          <line x1="22" y1="21" x2="30" y2="13" stroke="var(--alert-red)" stroke-width="2.4"/>
          <path d="M4 20 L26 36 L48 20 M4 48 L22 33 M48 48 L30 33" fill="none" stroke="#111" stroke-width="2"/>
        </svg>
        <div class="flag__body">
          <h3 class="flag__title">Suspicious Sender Address</h3>
          <p class="flag__text"><strong>Check the "from" email address carefully.</strong> It may look official but contain <strong>subtle misspellings, use a different domain</strong> (e.g., using @freemail.com instead of @bank.com), or not match the organization.</p>
        </div>
      </li>

      <li class="flag flag--hover">
        <svg class="flag__icon" viewBox="0 0 52 52" aria-hidden="true">
          <g stroke="#111" stroke-width="2" stroke-linecap="round">
            <line x1="6" y1="6" x2="10" y2="10"/><line x1="16" y1="2" x2="16" y2="7"/><line x1="2" y1="16" x2="7" y2="16"/><line x1="4" y1="26" x2="8" y2="23"/>
          </g>
          <path d="M18 10 L18 36 L24 30 L29 42 L34 40 L29 28 L37 28 Z" fill="var(--alert-red)" stroke="#111" stroke-width="2" stroke-linejoin="round"/>
        </svg>
        <div class="flag__body">
          <h3 class="flag__title">Hover Before You Click</h3>
          <p class="flag__text"><strong>Hover your mouse over any links or buttons to see the actual destination</strong> URL in the bottom corner of your browser. If it doesn't match the expected website, it is likely a scam.</p>
        </div>
      </li>

      <li class="flag flag--attach">
        <svg class="flag__icon" viewBox="0 0 52 52" aria-hidden="true">
          <path d="M36 14 L17 33 a5 5 0 0 0 7 7 L42 22 a9 9 0 0 0 -13 -13 L11 27 a13 13 0 0 0 18 18 L44 30" fill="none" stroke="var(--alert-red)" stroke-width="4" stroke-linecap="round"/>
        </svg>
        <div class="flag__body">
          <h3 class="flag__title">Unusual Attachments or Links</h3>
          <p class="flag__text">Be wary of <strong>unexpected attachments, especially .zip, .exe, or office documents,</strong> which can contain malware.</p>
        </div>
      </li>

      <li class="flag flag--offers">
        <svg class="flag__icon" viewBox="0 0 52 52" aria-hidden="true">
          <path d="M14 2 L24 22 M38 2 L28 22 M14 2 H22 L28 14 M38 2 H30" fill="var(--alert-red)" stroke="#111" stroke-width="2.4" stroke-linejoin="round"/>
          <circle cx="26" cy="34" r="15" fill="#fff" stroke="#111" stroke-width="2.4"/>
          <circle cx="26" cy="34" r="9" fill="none" stroke="#111" stroke-width="2"/>
          <path d="M26 28 L27.8 32 L32 32.3 L28.8 35 L29.8 39 L26 36.8 L22.2 39 L23.2 35 L20 32.3 L24.2 32 Z" fill="var(--alert-red)"/>
        </svg>
        <div class="flag__body">
          <h3 class="flag__title">Too-Good-To-Be-True Offers</h3>
          <p class="flag__text">Scams may promise <strong>unrealistic deals, prizes, or unexpected money,</strong> designed to lure you into clicking.</p>
        </div>
      </li>
    </ul>

    <section class="safety">
      <div class="safety__glow"></div>
      <h2 class="safety__title">How To<br>Be Safe</h2>
      <div class="safety__art" role="img" aria-label="Illustration of a woman unlocking a large phone with a fingerprint scan, with padlock and shield check icons"></div>

      <div class="tip tip--verify">
        <h3 class="tip__title">Verify<br>Independently</h3>
        <p class="tip__text">If you receive an urgent alert from a company, do not use the contact information in the email. Instead, find the company's official phone number or website separately.</p>
      </div>
      <div class="tip tip--mfa">
        <h3 class="tip__title">Enable Multi-Factor Authentication (MFA)</h3>
        <p class="tip__text">Set up MFA on all accounts, which provides a layer of security even if a password is stolen.</p>
      </div>
      <div class="tip tip--https">
        <h3 class="tip__title">Check<br>for https://</h3>
        <p class="tip__text">Legitimate websites use secure, encrypted connections, though this alone does not guarantee a site is safe.</p>
      </div>
      <div class="tip tip--browser">
        <h3 class="tip__title">Use Browser<br>Security</h3>
        <p class="tip__text">Browser password managers will often not auto-fill credentials on a fake phishing site, acting as a red flag.</p>
      </div>
    </section>

    <footer class="poster__footer">www.qrvlink.com | (555) 014-2738</footer>
  </article>

</body>
</html>
```